Velmora Systems 4-Brochure Package

Design an overall look-n-feel (a template). Then implement for a family of 4 brochures:
1. Unified Communications
2. App & Mobile Development
3. Telemedicine
4. Managed Services

Will need to incorporate content, diagrams, and photographs into each of the brochures (all provided).

Photographs need to be "layered" and colorized to match the overall brand concept of intersecting circles where the middle is the "velmora" (and the Q resides). See Concepts provided. (Colors: Pantone Blue 072C, Pantone 279C- 80% Opacity, Process Cyan 80% Opacity)

Utilize image "Velmora Infrastructure Background" as the background (refer to look of website listed below).

New website is under development and can be viewed at: http://brindlestudio-example.com/velmora/

Target Market(s)

Chief Information Officers and IT Professionals, Industries include health, hospitals, technology, manufacturing, government.

Industry/Entity Type

Communications

Requirements
Must have
• Need to use the blue-colorized photos (raw images provided). Need to match branded color palette (noted above in brief) - Refer to Brand Comps provided also.

Include both addresses:

SACRAMENTO:
1730 Kestrel Ridge Way, Suite 410
Sacramento, CA 95840
916.555.0142
Toll-free: 1.866.555.0197

CHICO:
468 Larkspur Lane, Suite 220
Chico, CA 95931
530.555.0168
Toll-free: 1.866.555.0197

```html
<!DOCTYPE html>
<html lang="en">
<head>
<meta charset="utf-8">
<title>Velmora Systems – Application and Mobile Development Brochure</title>
<link href="https://fonts.googleapis.com/css2?family=Didact+Gothic&family=Open+Sans:wght@600;700&display=swap" rel="stylesheet">
<style>
  :root{
    --navy:#1f4494;
    --brand-blue:#2a4fa0;
    --tab-blue:#6b9ad8;
    --cyan:#2aa8e0;
    --ink:#4a4a4a;
    --ink-dark:#2e2e2e;
    --paper:#ffffff;
    --backdrop:#ffffff;
    --infra-light:#e4eef9;
    --infra-mid:#c9dcf1;
  }
  *{margin:0;padding:0;box-sizing:border-box}
  html,body{width:1200px;height:1000px;overflow:hidden;background:var(--backdrop)}
  body{position:relative;font-family:"Didact Gothic",sans-serif;color:var(--ink)}
  .page{position:absolute;top:123px;width:570px;height:740px;overflow:hidden;
    box-shadow:2px 3px 6px rgba(0,0,0,.35)}
  .page--front{left:24px}
  .page--back{left:618px}
  .infra-bg{position:absolute;inset:0;
    background:
      repeating-linear-gradient(90deg,rgba(255,255,255,.0) 0 38px,rgba(255,255,255,.55) 38px 44px),
      repeating-linear-gradient(0deg,rgba(160,190,225,.25) 0 6px,rgba(255,255,255,0) 6px 22px),
      linear-gradient(180deg,#f7fafe 0%,var(--infra-light) 30%,var(--infra-mid) 100%)}
  .footer-band{position:absolute;left:0;right:0;top:627px;height:82px;background:var(--navy)}
  .panel{position:absolute;background:var(--paper)}
  .page--front .panel{left:30px;top:325px;width:510px;height:355px}
  .page--back .panel{left:32px;top:105px;width:510px;height:575px}

  .brand{position:absolute;right:10px;top:8px;width:78px;text-align:center}
  .brand__dot{width:44px;height:44px;border-radius:50%;background:var(--brand-blue);margin:0 auto 6px}
  .brand__name{font-family:"Didact Gothic",sans-serif;color:var(--brand-blue);font-size:13px;letter-spacing:.5px;line-height:1.05}
  .brand__name small{display:block;font-size:7px;letter-spacing:.8px}

  .title-box{position:absolute;left:0;top:99px;width:226px;height:61px;background:var(--navy);
    color:#fff;font-family:"Open Sans",sans-serif;font-weight:700;font-size:18.5px;line-height:24px;
    text-align:right;padding:7px 10px 0 0}

  .hero{position:absolute;left:190px;top:0;width:360px;height:420px}

  .intro{position:absolute;left:50px;top:446px;width:472px;font-size:10.4px;line-height:12.6px}
  .intro p+p{margin-top:12px}

  .features-tab{position:absolute;left:34px;top:97px;width:103px;height:25px;background:var(--navy);
    color:#fff;font-family:"Open Sans",sans-serif;font-weight:700;font-size:13px;line-height:25px;padding-left:18px}
  .features{position:absolute;left:42px;top:139px;width:498px;font-size:10.4px;line-height:12.6px}
  .features p{margin-bottom:9px}
  .features b{font-family:"Open Sans",sans-serif;font-weight:700;color:var(--ink-dark)}
  .cta{position:absolute;left:42px;top:371px;width:498px;font-family:"Open Sans",sans-serif;font-weight:700;
    font-size:10.4px;line-height:13px;color:var(--ink-dark)}

  .office-tab{position:absolute;left:32px;top:573px;width:122px;height:17px;background:var(--tab-blue);
    color:#fff;font-family:"Open Sans",sans-serif;font-weight:700;font-size:10.5px;line-height:17px;padding-left:20px;
    clip-path:polygon(0 0,92% 0,100% 50%,92% 100%,0 100%)}
  .office-brand{position:absolute;left:34px;top:600px;display:flex;align-items:center;gap:6px}
  .office-brand__dot{width:34px;height:34px;border-radius:50%;background:var(--brand-blue)}
  .office-brand__name{font-size:15px;color:var(--brand-blue);line-height:1}
  .office-brand__name small{display:block;font-size:8px;letter-spacing:.8px;margin-top:2px}
  .address{position:absolute;top:571px;font-size:11px;line-height:13.4px;color:var(--ink-dark)}
  .address--sac{left:176px}
  .address--chico{left:380px}
</style>
</head>
<body>

<section class="page page--front">
  <div class="infra-bg" role="img" aria-label="Pale blue tinted photo of server racks in a data centre"></div>
  <div class="footer-band"></div>
  <div class="panel"></div>

  <svg class="hero" viewBox="0 0 360 420" role="img" aria-label="Intersecting circles holding blue-tinted photos of hands using mobile devices">
    <defs>
      <linearGradient id="photoTop" x1="0" y1="0" x2="1" y2="1">
        <stop offset="0" stop-color="#9cc6ea"/><stop offset="1" stop-color="#3e7cc4"/>
      </linearGradient>
      <linearGradient id="photoBig" x1="0" y1="0" x2="1" y2="1">
        <stop offset="0" stop-color="#5fa2dc"/><stop offset="0.6" stop-color="#2f74c0"/><stop offset="1" stop-color="#1c4c9c"/>
      </linearGradient>
      <radialGradient id="photoCore" cx=".5" cy=".5" r=".6">
        <stop offset="0" stop-color="#8ad2f2"/><stop offset="1" stop-color="#2a8ad0"/>
      </radialGradient>
    </defs>
    <circle cx="210" cy="135" r="130" fill="url(#photoTop)" opacity=".85"/>
    <circle cx="190" cy="265" r="165" fill="url(#photoBig)" opacity=".92"/>
    <circle cx="285" cy="235" r="90" fill="#4aa9e4" opacity=".45"/>
    <circle cx="205" cy="228" r="72" fill="url(#photoCore)"/>
  </svg>

  <div class="title-box">Application and<br>Mobile Development</div>

  <div class="brand">
    <div class="brand__dot"></div>
    <div class="brand__name">VELMORA<small>SYSTEMS</small></div>
  </div>

  <div class="intro">
    <p>Velmora Systems and its affiliates have developed more than 400 apps for the mobile environment.&nbsp; Our application developers, designers, and program managers are experts at getting the right balance between client ideas, platform standards, and user experience while meeting technical and project challenges.&nbsp; Velmora ensures that we understand your application needs from a technical aspect while integrating its goal to meet business objectives.</p>
    <p>We offer complete, end-to-end services for mobile application development across all major platforms including Orchard Phone, Tessel’s Berrymark, Lumigo’s Andra, as well as Paneworks Mobile.&nbsp; Our application developers understand the components involved in SDK, Cacao Tap/Objective K, Zencode IDE, Layout Forge and many others.</p>
  </div>
</section>

<section class="page page--back">
  <div class="infra-bg" role="img" aria-label="Pale blue tinted photo of server racks in a data centre"></div>
  <div class="footer-band"></div>
  <div class="panel"></div>

  <div class="brand">
    <div class="brand__dot"></div>
    <div class="brand__name">VELMORA<small>SYSTEMS</small></div>
  </div>

  <div class="features-tab">Features</div>
  <div class="features">
    <p><b>Mobile Strategy</b> – We partner with you as a consultant to match your business requirements with the right solution.</p>
    <p><b>Design</b> – The aesthetic and user interface is the key determinant of an application’s success.&nbsp; Nothing beats a pleasing UI that delivers a smooth flowing user experience. Our award-winning design team is filled with creative artists who utilize trend-setting techniques and a rehearsed methodology to create the perfect user experience.</p>
    <p><b>Development</b> – With over 400 apps to our credit, we have one of the most experienced mobile application development teams in the world today.&nbsp; From simple games to complex enterprise level apps – we have done it all including integration into external hardware peripheral devices like credit card readers and armbands to monitor metabolic activities</p>
    <p><b>Industry Expertise</b> – From Finance and Healthcare to Travel and Education, Velmora and our affiliates have a wealth of cross-industry knowledge that we can bring to your application development project.</p>
  </div>
  <div class="cta">Call to Action: Email/Call/Click for more information on how you can put our Mobile and Application Development team to work for you.</div>

  <div class="office-tab">Office Address :</div>
  <div class="office-brand">
    <div class="office-brand__dot"></div>
    <div class="office-brand__name">VELMORA<small>SYSTEMS</small></div>
  </div>
  <address class="address address--sac" style="font-style:normal">
    SACRAMENTO:<br>1730 Kestrel Ridge Way, Suite 410<br>Sacramento, CA 95840<br>916.555.0142<br>Toll-free: 1.866.555.0197
  </address>
  <address class="address address--chico" style="font-style:normal">
    CHICO:<br>468 Larkspur Lane, Suite 220<br>Chico, CA 95931<br>530.555.0168<br>Toll-free: 1.866.555.0197
  </address>
</section>

</body>
</html>
```